Real State Agency App

We need an app design for a real state agency, we provide mockups for our project that ilustrates very well what we need
our web site is www.brindlevaleestates.com,

Target Market(s)

Tourism

Font styles to use
Other font styles liked:
• attached you will find it

Requirements
Must have
• Colors like the logo

```html
<!DOCTYPE html>
<html lang="en">
<head>
<meta charset="utf-8">
<title>Brindlevale Estates – App Screens</title>
<link href="https://fonts.googleapis.com/css2?family=Nunito:wght@500;600&family=Quicksand:wght@500;600&display=swap" rel="stylesheet">
<style>
  :root {
    --stage: #00a0c2;
    --stage-deep: #0a97b8;
    --screen: #ffffff;
    --brand-blue: #12357f;
    --brand-teal: #00a3c4;
    --brand-gold: #e2b62c;
    --tile: #e6e6e6;
    --ink: #2b2b2b;
    --muted: #444444;
    --plus: #2cc4b0;
    --sky-soft: #f4f4f4;
  }
  * { margin: 0; padding: 0; box-sizing: border-box; }
  html, body { width: 1200px; height: 1200px; overflow: hidden; }
  body {
    background: var(--stage);
    font-family: "Quicksand", sans-serif;
    position: relative;
  }
  .city-backdrop {
    position: absolute; left: 0; right: 0; bottom: 0; height: 320px;
    background: linear-gradient(180deg, rgba(0,160,194,0) 0%, rgba(20,180,210,0.35) 60%, rgba(20,180,210,0.5) 100%);
  }
  .screen-title {
    position: absolute; top: 108px; width: 429px; text-align: center;
    font-family: "Nunito", sans-serif; font-weight: 600; font-size: 38px;
    color: #ffffff; letter-spacing: 0.2px;
  }
  .phone {
    position: absolute; top: 177px; width: 429px; height: 761px;
    background: var(--screen); overflow: hidden;
  }
  .phone--splash { left: 145px; }
  .phone--home { left: 627px; }
  .title--splash { left: 145px; }
  .title--home { left: 627px; }

  .status-bar {
    position: absolute; top: 0; left: 0; right: 0; height: 24px;
    font-family: "Nunito", sans-serif; font-size: 13px; color: var(--ink);
  }
  .status-bar .signal { position: absolute; left: 6px; top: 6px; }
  .status-bar .time { position: absolute; left: 0; right: 0; top: 4px; text-align: center; font-size: 14px; }
  .status-bar .battery { position: absolute; right: 6px; top: 5px; display: flex; align-items: center; gap: 5px; font-size: 12px; }
  .battery-cell { width: 27px; height: 10px; background: #333; border-radius: 2px; position: relative; }
  .battery-cell::after { content: ""; position: absolute; right: -3px; top: 3px; width: 2px; height: 4px; background: #333; }

  .sky-scene {
    position: absolute; left: 0; right: 0; top: 24px; bottom: 0;
    background: linear-gradient(180deg, #ffffff 0%, #fafafa 50%, #f2f4f6 75%, #e9eef3 100%);
  }
  .skyline-faint {
    position: absolute; left: 0; right: 0; bottom: 0; height: 210px;
    background: linear-gradient(180deg, rgba(255,255,255,0) 0%, rgba(225,232,238,0.7) 60%, rgba(240,243,246,0.9) 100%);
  }
  .wordmark {
    position: absolute; left: 0; right: 0; text-align: center;
    font-family: "Quicksand", sans-serif; font-weight: 600;
    color: var(--brand-blue);
  }
  .wordmark--splash { top: 352px; font-size: 46px; }
  .wordmark--home { top: 140px; font-size: 42px; }

  .welcome {
    position: absolute; top: 92px; left: 0; right: 0; text-align: center;
    font-size: 19px; letter-spacing: 9px; color: var(--ink); font-weight: 500;
  }
  .info-badge { position: absolute; left: 390px; top: 41px; }
  .menu-grid { position: absolute; left: 0; top: 0; }
  .menu-label {
    position: absolute; width: 160px; text-align: center;
    font-size: 19px; line-height: 18px; color: var(--ink); font-weight: 500; letter-spacing: 0.6px;
  }
  .menu-label--search { left: 33px; top: 430px; }
  .menu-label--sell { left: 234px; top: 430px; }
  .menu-label--service { left: 134px; top: 531px; }
  .tile-wordmark {
    position: absolute; left: 134px; top: 320px; width: 160px; text-align: center;
    font-size: 20px; font-weight: 600; color: #ffffff;
  }
  .language-picker {
    position: absolute; left: 275px; top: 713px; display: flex; align-items: center; gap: 12px;
    font-size: 20px; color: var(--ink); font-weight: 500;
  }
</style>
</head>
<body>
  <div class="city-backdrop" role="img" aria-label="Faint city skyline illustration across the background"></div>

  <div class="screen-title title--splash">Splash</div>
  <div class="screen-title title--home">Home/Menu</div>

  <!-- Splash screen -->
  <section class="phone phone--splash">
    <div class="sky-scene" role="img" aria-label="Illustration of soft clouds over a pastel city skyline"></div>
    <div class="status-bar">
      <svg class="signal" width="60" height="12" viewBox="0 0 60 12">
        <g fill="#333"><circle cx="4" cy="6" r="3"/><circle cx="12" cy="6" r="3"/><circle cx="20" cy="6" r="3"/><circle cx="28" cy="6" r="3"/><circle cx="36" cy="6" r="3"/></g>
        <path d="M46 5 q6 -5 12 0 M48.5 7.5 q3.5 -3 7 0" stroke="#333" stroke-width="1.5" fill="none"/><circle cx="52" cy="10" r="1.2" fill="#333"/>
      </svg>
      <div class="time">9:23 PM</div>
      <div class="battery">100% <span class="battery-cell"></span></div>
    </div>
    <div class="wordmark wordmark--splash">Brindlevale</div>
  </section>

  <!-- Home / Menu screen -->
  <section class="phone phone--home">
    <div class="skyline-faint" role="img" aria-label="Faded city skyline illustration along the bottom"></div>
    <div class="status-bar">
      <svg class="signal" width="60" height="12" viewBox="0 0 60 12">
        <g fill="#333"><circle cx="4" cy="6" r="3"/><circle cx="12" cy="6" r="3"/><circle cx="20" cy="6" r="3"/><circle cx="28" cy="6" r="3"/><circle cx="36" cy="6" r="3"/></g>
        <path d="M46 5 q6 -5 12 0 M48.5 7.5 q3.5 -3 7 0" stroke="#333" stroke-width="1.5" fill="none"/><circle cx="52" cy="10" r="1.2" fill="#333"/>
      </svg>
      <div class="time">9:23 PM</div>
      <div class="battery">100% <span class="battery-cell"></span></div>
    </div>

    <svg class="info-badge" width="22" height="22" viewBox="0 0 22 22">
      <circle cx="11" cy="11" r="11" fill="var(--brand-gold)"/>
      <circle cx="11.8" cy="6" r="1.6" fill="#fff"/>
      <path d="M10 9.5 h2.6 l-1.3 6.5 h1.5" stroke="#fff" stroke-width="2" fill="none" stroke-linecap="round"/>
    </svg>

    <div class="welcome">Welcome to</div>
    <div class="wordmark wordmark--home">Brindlevale</div>

    <svg class="menu-grid" width="429" height="761" viewBox="0 0 429 761">
      <polygon points="113,323 211,421 113,519 15,421" fill="var(--tile)"/>
      <polygon points="315,323 413,421 315,519 217,421" fill="var(--tile)"/>
      <polygon points="214,424 312,522 214,620 116,522" fill="var(--tile)"/>
      <polygon points="214,251 296,333 214,415 132,333" fill="var(--brand-teal)"/>
      <!-- search icon -->
      <circle cx="119" cy="387" r="14" fill="#bfe9f2" stroke="var(--brand-teal)" stroke-width="3"/>
      <line x1="109" y1="397" x2="100" y2="406" stroke="#222" stroke-width="3" stroke-linecap="round"/>
      <line x1="92" y1="410" x2="126" y2="410" stroke="#d9332b" stroke-width="1.5"/>
      <!-- sell icon -->
      <circle cx="315" cy="391" r="24" fill="var(--plus)"/>
      <path d="M315 379 v24 M303 391 h24" stroke="#fff" stroke-width="1.6"/>
      <!-- service icon -->
      <rect x="190" y="479" width="26" height="14" rx="7" fill="none" stroke="var(--brand-gold)" stroke-width="3"/>
      <rect x="208" y="485" width="26" height="14" rx="7" fill="none" stroke="var(--brand-blue)" stroke-width="3"/>
      <line x1="188" y1="507" x2="238" y2="507" stroke="#2fbf4a" stroke-width="3"/>
      <!-- globe -->
      <circle cx="289" cy="726" r="12" fill="none" stroke="var(--brand-blue)" stroke-width="3"/>
      <ellipse cx="289" cy="726" rx="5" ry="12" fill="none" stroke="var(--brand-blue)" stroke-width="2"/>
      <line x1="277" y1="726" x2="301" y2="726" stroke="var(--brand-blue)" stroke-width="2"/>
      <!-- chevron -->
      <path d="M401 729 l6 -6 l6 6" fill="none" stroke="#222" stroke-width="1.8"/>
    </svg>

    <div class="tile-wordmark">Brindlevale</div>
    <div class="menu-label menu-label--search">Search<br>Properties</div>
    <div class="menu-label menu-label--sell">Sell<br>Property</div>
    <div class="menu-label menu-label--service">Our<br>Service</div>
    <div class="language-picker" style="left:313px;">English</div>
  </section>
</body>
</html>
```